Brochure to advertise our unique physiotherapy clinic to general practitioners

We want to advertise our unique physiotherapy clinic to general practitioners (GPs) to develop there awareness of both our existence and services offered. The brochure should highlight our uniqueness (i.e. providing the highest quality care, advice and education) based on our expert research-based knowledge and skills. After reading the brochure, we want GPs to feel like they know us a little and feel happy to refer their patients to our clinic.
Attached is a draft flyer containing our logo, contact details, profile pictures and the information we would like to be contained in the brochure. We would like the brochure to be A4 double sided and able to be folded to fit into an envelope. More material (pictures) and understanding of our clinic can be found at www.kinetreva.com.au

A brief background of our team:
Our team currently consists of two physiotherapists specialising in the management of musculoskeletal and sports injuries, Dr Howard Tenniscombe and Dr Lionel Fairweather. Both Howard and Lionel have completed PhDs related to musculosketal injury management, and continue to be actively involved in international research groups. Between them they have authored more than 50 peer reviewed papers, presented at countless national and international conferences, and coordinate numerous courses to facilitate professional development of other clinicians. Most importantly, they continue to enjoy mixing these research and teaching activities with treating patients.

Updates
Project Deadline Extended
Reason: Consultation with clinic partner is needed and to allow time for modifications and additional designs. We will pick one, just want quality.
Thanks

Project Deadline Extended

Thank you for some great designs thus far everyone. We have decided to remove the fees from the brochure so please do the same for any future submissions. In the process of trying to provide feedback now.
Thanks
Project Deadline Extended
Reason: A couple of designs are close and we want to allow time to make appropriate modifications. This will be the last extension. Thanks for everyones effort so far

Project Deadline Extended

Target Market(s)
Australian General Practitioners and other health professionals are the targeted audience
Industry/Entity Type
Clinic
Look and feel

```html
<!DOCTYPE html>
<html lang="en">
<head>
<meta charset="utf-8">
<title>Kinetreva – Successfully treating difficult injuries for life</title>
<link href="https://fonts.googleapis.com/css2?family=Arimo:wght@400;700&display=swap" rel="stylesheet">
<style>
  :root{
    --blue:#3d9fdb;
    --navy:#0d3a86;
    --green:#a3d21e;
    --green-dark:#8cbf12;
    --white:#ffffff;
    --ink:#333333;
    --grey:#6b6b6b;
  }
  *{box-sizing:border-box;margin:0;padding:0}
  html,body{width:1200px;height:927px;overflow:hidden;background:#fff}
  body{font-family:"Arimo",Arial,sans-serif}
  .brochure{position:relative;width:1200px;height:927px;overflow:hidden}
  .panel{position:absolute;top:0;height:927px;overflow:hidden}

  /* Team panel */
  .panel-team{left:0;width:405px;background:var(--blue);color:var(--white)}
  .team-hero{position:absolute;left:0;top:0}
  .bio{position:absolute;left:10px;width:390px;font-size:11px;letter-spacing:0.35px;line-height:11.7px}
  .bio-howard{top:278px}
  .bio-lionel{top:618px}
  .bio-portrait{float:left;width:175px;height:133px;margin:3px 4px 2px 0}
  .bio-portrait-howard{background:linear-gradient(160deg,#9aa58e,#3b4a63 70%,#2a3550)}
  .bio-portrait-lionel{background:linear-gradient(160deg,#4f6a2c,#86965a 55%,#e9ecef 80%)}
  .bio-name{font-weight:700;font-size:11.5px;letter-spacing:0;text-align:center;padding-left:180px;line-height:13px}
  .bio p{margin:0}

  /* Contact panel */
  .panel-contact{left:405px;width:393px;background:var(--white)}
  .contact-swoosh{position:absolute;left:0;bottom:0}
  .brand{position:absolute;display:flex;align-items:center;gap:10px}
  .brand-dot{width:40px;height:40px;border-radius:50%;background:var(--blue);flex:none}
  .brand-name{font-weight:700;color:var(--ink);letter-spacing:-0.5px;line-height:1}
  .brand-tagline{position:absolute;color:var(--grey);font-size:10px;white-space:nowrap}
  .brand-contact{left:45px;top:680px}
  .brand-contact .brand-name{font-size:34px}
  .tagline-contact{left:150px;top:740px}
  .contact-details{position:absolute;left:0;width:393px;top:762px;text-align:center;color:var(--blue);font-weight:700;font-size:14.5px;line-height:18.4px;list-style:none}

  /* Cover panel */
  .panel-cover{left:798px;width:402px;background:var(--blue)}
  .cover-hero{position:absolute;left:0;top:0}
  .cover-band{position:absolute;left:0;top:535px;width:402px;height:66px;background:var(--navy);color:var(--green);font-weight:700;font-size:24px;line-height:28px;text-align:center;padding-top:4px}
  .cover-title{position:absolute;left:0;top:606px;width:402px;text-align:center;color:var(--white);font-weight:700;font-size:64px;line-height:72px;letter-spacing:1px}
  .cover-rule{position:absolute;left:0;top:682px;width:402px;height:2px;background:var(--white)}
  .cover-foot{position:absolute;left:0;bottom:0}
  .brand-cover{left:30px;top:820px}
  .brand-cover .brand-dot{width:50px;height:50px}
  .brand-cover .brand-name{font-size:44px}
  .tagline-cover{left:192px;top:880px;font-size:11px}
</style>
</head>
<body>
<main class="brochure">

  <section class="panel panel-team">
    <svg class="team-hero" width="405" height="270" viewBox="0 0 405 270">
      <path d="M0 235 Q190 270 405 160 V200 Q200 290 0 262 Z" fill="var(--green)"/>
      <path d="M0 222 Q200 262 405 140 V165 Q200 275 0 240 Z" fill="var(--white)"/>
      <path d="M0 0 H380 Q392 120 340 170 Q220 240 0 210 Z" fill="#4a5670" role="img" aria-label="Portrait photo of a smiling physiotherapist"/>
    </svg>

    <article class="bio bio-howard">
      <div class="bio-portrait bio-portrait-howard" role="img" aria-label="Portrait photo of Dr Howard Tenniscombe"></div>
      <h2 class="bio-name">Dr Howard Tenniscombe</h2>
      <p>Dr Howard Tenniscombe is an expert physiotherapist with extensive expertise in managing sports injuries and back pain and a international clinical and research profile in tendinopathy management. He completed his undergraduate physiotherapy degree at Larkfield University in 1996, and his PhD in 2006.</p>
      <p>Howard has been consulted to some of the worlds best athletes, including Southern Institute of Sport athletes, elite basketball and volleyball players, elite premier league football players (e.g. Northgate United FC, Riverside FC, Eastvale City FC), elite rugby players (e.g. Highland Rugby international squad players), the Crown Ballet (London) and top-level National Institute of Sport and United Kingdom track athletes, among others (read more). He is often consulted to treat difficult and unresolving injuries that have not responded to treatment.</p>
      <p>Howard has published on tendinopathy, groin pain, patellofemoral joint injury, biomechanics, rehabilitation, physiology and running technique. He has lectured to physiotherapists, and other health professionals all over the world in his area of expertise. He is currently a Visiting Senior Lecturer at Kingsbridge University (London).</p>
    </article>

    <article class="bio bio-lionel">
      <div class="bio-portrait bio-portrait-lionel" role="img" aria-label="Portrait photo of Dr Lionel Fairweather"></div>
      <h2 class="bio-name">Dr Lionel Fairweather</h2>
      <p>Lionel qualified as a physiotherapist in 2005 in Australia, and completed his PhD relating to knee pain, foot orthotics and lower limb biomechanics in 2010. At various private practices and sports medicine centres in Australia and London he has combined his strong research background with a strong passion and ability to treat a wide range of patients, from sedentary to high level sports. Lionel continues to combine research with clinical practice, maintaining part time research roles including Masters Student supervision in the 'Harbourline Centre for Movement Health' at Kingsbridge University of London; and as Research Director at the largest Sports Medicine Centre in London. In the clinic, Lionel enjoys combining an extensive range of hands on interventions with exercise prescription. Additionally, due to his research background he also has exceptional skills to complete comprehensive biomechanical assessments, and provide foot orthotic advice and prescription where necessary. Put together, these skills will ensure you the greatest chance for a full or optimal recovery from almost any injury.</p>
    </article>
  </section>

  <section class="panel panel-contact">
    <svg class="contact-swoosh" width="393" height="130" viewBox="0 0 393 130">
      <path d="M0 130 V85 Q230 100 393 0 V130 Z" fill="var(--green)"/>
    </svg>
    <div class="brand brand-contact">
      <span class="brand-dot"></span>
      <span class="brand-name">Kinetreva</span>
    </div>
    <span class="brand-tagline tagline-contact">Expert care. Research-led recovery</span>
    <ul class="contact-details">
      <li>Level 4, 22-24</li>
      <li>Marlow Avenue Ashbury East 3127</li>
      <li>Phone: (03) 9555 0142</li>
      <li>Email: info@kinetreva.com.au</li>
      <li>www.kinetreva.com.au</li>
    </ul>
  </section>

  <section class="panel panel-cover">
    <svg class="cover-hero" width="402" height="530" viewBox="0 0 402 530">
      <defs>
        <linearGradient id="sky" x1="0" y1="0" x2="0" y2="1">
          <stop offset="0" stop-color="#2f6fc0"/>
          <stop offset="0.5" stop-color="#7fb2e2"/>
          <stop offset="1" stop-color="#3b3b44"/>
        </linearGradient>
      </defs>
      <path d="M60 0 H402 V520 Q200 540 60 430 Q-10 330 10 160 Q25 50 60 0 Z" fill="var(--green)"/>
      <path d="M70 0 H402 V505 Q230 530 100 430 Q28 340 40 160 Q50 50 70 0 Z" fill="var(--white)"/>
      <path d="M78 0 H402 V495 Q240 520 110 425 Q40 335 52 160 Q62 55 78 0 Z" fill="url(#sky)" role="img" aria-label="Photo of a cyclist in a red jersey and helmet riding a road bike"/>
    </svg>
    <h1 class="cover-band">Successfully treating<br>difficult injuries</h1>
    <p class="cover-title">FOR LIFE</p>
    <div class="cover-rule"></div>
    <svg class="cover-foot" width="402" height="170" viewBox="0 0 402 170">
      <path d="M0 170 V0 H402 V170 Z" fill="var(--green)"/>
      <path d="M0 160 Q200 150 402 110 V170 H0 Z" fill="var(--green-dark)"/>
    </svg>
    <div class="brand brand-cover">
      <span class="brand-dot"></span>
      <span class="brand-name">Kinetreva</span>
    </div>
    <span class="brand-tagline tagline-cover">Expert care. Research-led recovery</span>
  </section>

</main>
</body>
</html>
```